Flyer Design

We are a property company and need attractive flyers that will grab peoples attention. We want them to be bold but simple and not too busy. I attach a draft and also our logo. We will print in A5 size.
Thank you & I look forward to receiving designs.

It Company

```html
<!DOCTYPE html>
<html lang="en">
<head>
<meta charset="utf-8">
<title>Nova Developments – Subdivision Flyer</title>
<link href="https://fonts.googleapis.com/css2?family=Chakra+Petch:wght@700&family=Roboto+Condensed:wght@400;500&family=Roboto:wght@400&display=swap" rel="stylesheet">
<style>
  :root {
    --page-bg: #e9e8e8;
    --paper: #ffffff;
    --photo-light: #eef2f6;
    --photo-mid: #c9d5e2;
    --photo-deep: #8fa3ba;
    --bubble-red: #d0202a;
    --bubble-blue: #233f92;
    --accent-orange: #f0936a;
    --band-dark: #7f1f22;
    --band-light: #d9a9ab;
    --maroon-text: #7d1c22;
    --brand-brown: #6f4a22;
    --ink: #222222;
    --white: #ffffff;
  }
  * { box-sizing: border-box; margin: 0; padding: 0; }
  html, body { width: 1200px; height: 1200px; overflow: hidden; }
  body { background: var(--page-bg); position: relative; }

  .flyer {
    position: absolute; left: 190px; top: 25px;
    width: 820px; height: 1150px;
    background: var(--paper);
    overflow: hidden;
    box-shadow: 0 6px 18px rgba(0,0,0,0.18);
  }

  .hero-photo {
    position: absolute; left: 0; top: 0; width: 820px; height: 600px;
    background:
      radial-gradient(ellipse at 80% 30%, var(--photo-deep) 0%, rgba(143,163,186,0) 45%),
      radial-gradient(ellipse at 15% 5%, var(--photo-deep) 0%, rgba(143,163,186,0) 35%),
      linear-gradient(180deg, var(--photo-mid) 0%, var(--photo-light) 60%, var(--paper) 100%);
  }

  .bubble {
    position: absolute;
    font-family: "Chakra Petch", sans-serif;
    font-weight: 700;
    font-variant: small-caps;
    text-transform: lowercase;
    color: var(--white);
    letter-spacing: 1px;
  }
  .bubble svg.tail { position: absolute; overflow: visible; }

  .bubble--question {
    left: 37px; top: 30px; width: 455px; height: 225px;
    background: var(--bubble-red);
    padding: 20px 30px;
    font-size: 42px; line-height: 35px;
  }
  .bubble--question .tail { left: 380px; top: 224px; }

  .bubble--mortgage {
    left: 460px; top: 345px; width: 300px; height: 190px;
    background: var(--bubble-blue);
    padding: 20px 30px;
    font-size: 42px; line-height: 38px;
  }
  .bubble--mortgage .tail { left: 18px; top: 189px; }
  .bubble--mortgage .highlight { color: var(--accent-orange); }

  .promise-band {
    position: absolute; left: 0; top: 600px; width: 820px; height: 250px;
    background: linear-gradient(180deg, var(--band-dark) 0%, #9a3d40 55%, var(--band-light) 100%);
    color: var(--white);
    font-family: "Roboto Condensed", sans-serif;
    font-weight: 400;
    padding: 28px 60px;
    text-transform: uppercase;
  }
  .promise-band p { line-height: 1; white-space: nowrap; }
  .promise-band .small { font-size: 48px; }
  .promise-band .large { font-size: 68px; }
  .promise-band .line1 { margin-bottom: 8px; }
  .promise-band .line2 { margin-bottom: 4px; }

  .call-to-action {
    position: absolute; left: 0; top: 890px; width: 820px;
    text-align: center;
    font-family: "Chakra Petch", sans-serif;
    font-weight: 700;
    font-variant: small-caps;
    text-transform: lowercase;
    color: var(--maroon-text);
    font-size: 42px; line-height: 42px;
  }

  .contact-list {
    position: absolute; left: 45px; top: 1065px;
    list-style: none;
    font-family: "Roboto", sans-serif;
    font-size: 18px; line-height: 25px;
    color: var(--ink);
  }
  .contact-list li { display: flex; align-items: center; gap: 7px; }
  .contact-list svg { width: 15px; height: 15px; fill: var(--ink); }

  .brand-name {
    position: absolute; right: 50px; top: 1085px;
    display: flex; align-items: center; gap: 12px;
    font-family: "Roboto Condensed", sans-serif;
    font-weight: 500;
    font-size: 36px;
    letter-spacing: 2px;
    color: var(--brand-brown);
    text-transform: uppercase;
  }
  .brand-name .mark { width: 18px; height: 18px; background: var(--brand-brown); border-radius: 50%; }
</style>
</head>
<body>
  <main class="flyer">
    <div class="hero-photo" role="img" aria-label="Soft blue-toned photo of a calculator, stacked coins and a financial line chart"></div>

    <div class="bubble bubble--question">
      Are you a homeowner looking for financial freedom while been able to keep your own home?
      <svg class="tail" width="70" height="70" viewBox="0 0 70 70"><polygon points="0,0 70,0 65,60" fill="var(--bubble-red)"/></svg>
    </div>

    <div class="bubble bubble--mortgage">
      <span class="highlight">Are you</span><br>
      struggling<br>
      <span class="highlight">to pay your</span><br>
      mortgage?
      <svg class="tail" width="80" height="40" viewBox="0 0 80 40"><polygon points="0,0 80,0 0,35" fill="var(--bubble-blue)"/></svg>
    </div>

    <section class="promise-band">
      <p class="line1 small">Nova specialise in</p>
      <p class="line2"><span class="large">Subdivisions</span> <span class="small">including</span></p>
      <p class="line3"><span class="large">Finance</span> <span class="small">and</span> <span class="large">Management.</span></p>
    </section>

    <p class="call-to-action">Find out if your property is suitable<br>for subdivision in Auckland</p>

    <ul class="contact-list">
      <li><svg viewBox="0 0 16 16"><path d="M3 2l3 0 1 4-2 1c1 2 2 3 4 4l1-2 4 1 0 3c0 1-1 2-2 2C6 15 1 10 1 4c0-1 1-2 2-2z"/></svg>021 555 0148</li>
      <li><svg viewBox="0 0 16 16"><path d="M1 3h14v10H1z M2 4l6 5 6-5" fill="none" stroke="var(--ink)" stroke-width="1.5"/></svg>info@novasubdivide.com</li>
      <li><svg viewBox="0 0 16 16"><circle cx="8" cy="8" r="6.5" fill="none" stroke="var(--ink)" stroke-width="1.4"/><path d="M1.5 8h13M8 1.5c-3 3-3 10 0 13M8 1.5c3 3 3 10 0 13" fill="none" stroke="var(--ink)" stroke-width="1.2"/></svg>www.novasubdivide.com</li>
    </ul>

    <div class="brand-name"><span class="mark"></span>Nova Developments</div>
  </main>
</body>
</html>
```